Honey Bottle Labels for Honey Business

The honey is a niche product and the logo should exude a strong impression of wild and raw honey and natural – as in natural beekeeping. We try to keep things as simple as possible; this includes the processes the honey goes through.
We are looking for something with a gourmet / classy upmarket look and feel design. For example: Ideas with bees, honeycomb, modern or hexagonal feature; something eye catching, but not too busy.
Our honey is all natural and organic. We are a clean, simple yet sophisticated business, so would like our logo to reflect these principles.

Feel free to expand your creativity to anything you may think would look awesome and original!

The label needs to contain:
1. Our company logo. (Please see attached)
2. 100% Pure Raw Honey / Local
3. Net Wt: 16 oz (454 g) (this is the weight of the honey and will need to be modified based on bottle size.)
4. Address, Cedar Bend, MN 56000 (not larger than 1/16th inch)

Needs to be versatile to include possibility of clear label, I have included some example pictures as ideas (oval, round, square tags)

Sizes needed:
Large oval 2 5/8" x 4 1/2"
Small oval: 1 3/4" wide x 3" tall
Rectangle 1 3/4" tall x 5" wide
Round diameter 2.5"

Target Market(s)

Gourmet stores, market stall, local tourist market, potential store door sales

Requirements
Must have
• - A design that can be used on various packaging, jars and containers. We are hoping to scale up the production and want something to suit.
• - has to have a wow to stand out on the supermarket shelves
Nice to have
• Things we like:
• Minimalist designs
• Clever designs
• We don't like hand drawn font types
• We are open to the use of a hexagon in the logo, but not must have
Should not have
• Things we do not like:
• Too many colors

```html
<!DOCTYPE html>
<html lang="en">
<head>
<meta charset="utf-8">
<title>Meadow Hollow Honey – Jar Label</title>
<link href="https://fonts.googleapis.com/css2?family=Fira+Sans:wght@400;500;600&display=swap" rel="stylesheet">
<style>
  :root {
    --page: #ffffff;
    --cream: #faf3c8;
    --amber: #f7a81b;
    --amber-light: #fbbf2c;
    --amber-deep: #f39a12;
    --band: #d9893a;
    --ink: #2e2416;
    --comb-dark: #4a2a12;
    --white: #ffffff;
    --leaf-soft: #cfe6b4;
  }
  * { box-sizing: border-box; margin: 0; padding: 0; }
  html, body {
    width: 1200px; height: 1200px; overflow: hidden;
    background: var(--page);
    font-family: "Fira Sans", Arial, sans-serif;
  }
  .label {
    position: absolute; left: 71px; top: 185px;
    width: 1058px; height: 829px;
    background: var(--cream);
  }
  .comb-strip {
    position: absolute; left: 443px; top: 0;
    width: 165px; height: 160px;
    background: linear-gradient(180deg, #f6a21c 0%, #fbb63a 60%, #f39a12 100%);
    border-left: 5px solid var(--comb-dark);
    border-right: 5px solid var(--comb-dark);
  }
  .tag {
    position: absolute; left: 256px; top: 151px;
    width: 536px; height: 619px;
    border-radius: 268px 268px 0 0;
    background: var(--white);
    padding: 13px 13px 0;
  }
  .tag-body {
    width: 100%; height: 100%;
    border-radius: 255px 255px 0 0;
    background: linear-gradient(180deg, var(--amber-deep) 0%, var(--amber) 45%, var(--amber-light) 100%);
  }
  .flower {
    position: absolute; left: 460px; top: 130px;
    width: 130px; height: 90px;
    border-radius: 12px;
    background: linear-gradient(180deg, var(--white) 0%, var(--leaf-soft) 100%);
  }
  .seal {
    position: absolute; left: 324px; top: 219px;
    width: 400px; height: 400px; border-radius: 50%;
    background: var(--white);
    display: flex; align-items: center; justify-content: center;
  }
  .seal-ring {
    width: 372px; height: 372px; border-radius: 50%;
    border: 5px solid var(--amber);
    display: flex; flex-direction: column; align-items: center; justify-content: center;
    gap: 18px;
    padding-top: 20px;
  }
  .brand-dot {
    width: 56px; height: 56px; border-radius: 50%;
    background: var(--amber);
  }
  .brand-name {
    color: var(--amber);
    font-weight: 400; font-size: 42px; line-height: 1.05;
    text-align: center; white-space: nowrap;
  }
  .claim {
    position: absolute; left: 256px; width: 536px; top: 632px;
    text-align: center; color: var(--ink);
  }
  .claim-percent { font-weight: 600; font-size: 24px; letter-spacing: 1px; }
  .claim-line {
    display: flex; align-items: center; justify-content: center;
    margin-top: 2px;
  }
  .claim-line svg { flex: none; }
  .claim-text {
    font-weight: 600; font-size: 24px; letter-spacing: 1.5px;
    padding: 0 6px;
  }
  .address {
    position: absolute; left: 256px; width: 536px; top: 715px;
    text-align: center; color: var(--ink);
    font-weight: 400; font-size: 19px; letter-spacing: 2.5px;
  }
  .weight-band {
    position: absolute; left: 0; top: 770px;
    width: 1058px; height: 59px;
    background: var(--band);
    display: flex; align-items: center; justify-content: center;
    color: var(--ink); font-size: 18px; letter-spacing: 1.5px;
  }
</style>
</head>
<body>
  <div class="label">
    <div class="comb-strip" role="img" aria-label="Honeycomb with dripping honey"></div>

    <div class="tag"><div class="tag-body" role="img" aria-label="Amber hexagon honeycomb pattern"></div></div>

    <div class="flower" role="img" aria-label="White daisy with green leaves"></div>

    <div class="seal">
      <div class="seal-ring">
        <div class="brand-dot"></div>
        <div class="brand-name">meadow hollow<br>honey</div>
      </div>
    </div>

    <div class="claim">
      <div class="claim-percent">100%</div>
      <div class="claim-line">
        <svg width="72" height="24" viewBox="0 0 72 24" aria-hidden="true">
          <polygon points="2,12 7,3 17,3 22,12 17,21 7,21" fill="var(--comb-dark)"/>
          <line x1="24" y1="12" x2="70" y2="12" stroke="var(--ink)" stroke-width="2" stroke-dasharray="6 4"/>
        </svg>
        <span class="claim-text">PURE RAW HONEY</span>
        <svg width="72" height="24" viewBox="0 0 72 24" aria-hidden="true">
          <line x1="2" y1="12" x2="48" y2="12" stroke="var(--ink)" stroke-width="2" stroke-dasharray="6 4"/>
          <polygon points="50,12 55,3 65,3 70,12 65,21 55,21" fill="var(--comb-dark)"/>
        </svg>
      </div>
    </div>

    <div class="address">CEDAR BEND, MN 56000</div>

    <div class="weight-band">NET WT: 16 OZ (454 G)</div>
  </div>
</body>
</html>
```